Plakat für Fußballturnier-Wochenende
Zielgruppe
Wir sind eine IT-Firma und richten jedes Jahr ein Fußballwochenende / Fußballcup aus. Die Zielgruppe des Plakats sind die Anwohner der Gemeinde.
Aufgabenstellung
An den Ortseingängen der Gemeinde Wendelsau stehen Ortsinformationstafeln welche immer für den Aufzug von aktuellen Veranstaltungen genutzt werden. Dies sind quasi Stahlträger auf welche Plakate aufgezogen werden. Hierfür soll ein Plakat erstellt werden. Ebenfalls soll dies auch in sozialen Medien gestreut werden und im lokalen Wochenblatt (A4
) abgedruckt werden.
Auf dem Plakat soll zu sehen sein:
- Logo Brenner & Kluge Cup
- Logo SpVgg Wendelsau
- 7. Brenner & Kluge Cup (das ist quasi das Dach der Veranstaltung)
- Datum: 07. - 09.06.2024
- Ort: Sportpark Lindenwiese
- Freitag: Elfmeterturnier mit Live-Band
- Samstag: Jugendturnier F- und C- Jugend Vormittags und E-Jugend Nachmittags
- Sonntag: Jugendturnier B- und D- Jugend Vormittags und F3-Jugend Nachmittags
- Logo der Band
- Besucher sind Willkommen; Leibliche Wohl ist gesorgt.
- Der Gras Hintergrund ist Optional - muss nicht zwingend dazu
Informationen von der Firma welche den Druck der großen Plakate ausführt:
Die Schilder sind 110cm x 160cm, wenn sie das auf einer Plane(Banner) haben wollen, kommen noch 8 Ösen rein, 2cm vom Rand. Die Grafik sollte am besten auf Originalgröße angelegt werden und abspeichern als PDF.
Die Dateien sollten auch in einer veränderbaren Form zur Verfügung gestellt werden.

```html
<!DOCTYPE html>
<html lang="de">
<head>
<meta charset="utf-8">
<title>Brenner &amp; Kluge Cup 2024</title>
<link href="https://fonts.googleapis.com/css2?family=Baloo+2:wght@600;700&family=Cabin:wght@500&display=swap" rel="stylesheet">
<style>
  :root {
    --grass-dark: #2f7a1c;
    --grass-light: #5aa532;
    --line: #ffffff;
    --red: #c0302b;
    --band-green: #4c9a3a;
    --grey: #b4b4b4;
    --circle-fill: rgba(240, 240, 240, 0.93);
  }
  html, body { margin: 0; padding: 0; overflow: hidden; }
  .poster {
    position: relative;
    width: 1200px;
    height: 625px;
    overflow: hidden;
    font-family: "Baloo 2", sans-serif;
  }
  .grass {
    position: absolute; inset: 0;
    background: radial-gradient(ellipse at 40% 40%, var(--grass-light), var(--grass-dark));
  }
  .pitch { position: absolute; inset: 0; }
  .cup-mark {
    position: absolute;
    left: 478px; top: 218px;
    width: 240px;
    text-align: center;
  }
  .cup-mark .square {
    display: block;
    width: 116px; height: 116px;
    margin: 0 auto 18px;
    background: var(--grey);
  }
  .cup-mark .name {
    font-family: "Cabin", sans-serif;
    font-weight: 500;
    color: var(--red);
    font-size: 24px;
    line-height: 1.2;
    letter-spacing: 0.5px;
  }
  .badge {
    position: absolute;
    border-radius: 50%;
    display: flex; align-items: center; justify-content: center;
    text-align: center;
    font-weight: 700;
    line-height: 1.05;
  }
  .badge.band { left: 915px; top: 51px; width: 108px; height: 108px; background: var(--band-green); color: #fff; font-size: 17px; }
  .badge.club { left: 1044px; top: 50px; width: 110px; height: 110px; background: #fff; color: var(--band-green); font-size: 15px; }
  .venue {
    position: absolute;
    left: 763px; top: 271px;
    width: 150px; height: 150px;
    border-radius: 50%;
    background: #fff;
    display: flex; align-items: center; justify-content: center;
    text-align: center;
    color: var(--red);
    font-size: 18px;
    font-weight: 600;
    line-height: 1.1;
  }
  .venue span { transform: rotate(-10deg); }
  .schedule {
    position: absolute;
    left: 820px; top: 252px;
    width: 400px;
    color: #fff;
    text-align: center;
    transform: rotate(-8deg);
    transform-origin: center top;
    font-weight: 600;
    font-size: 15px;
    line-height: 1.15;
  }
  .schedule .date { font-size: 34px; font-weight: 700; line-height: 1.05; margin-bottom: 18px; }
  .schedule .day { margin-top: 14px; }
  .schedule .day:first-of-type { margin-top: 0; }
  .schedule .label { font-size: 15px; }
  .schedule .welcome { margin-top: 22px; }
</style>
</head>
<body>
<div class="poster">
  <div class="grass" role="img" aria-label="Rasenfläche aus der Vogelperspektive"></div>

  <svg class="pitch" width="1200" height="625" viewBox="0 0 1200 625" aria-hidden="true">
    <g fill="none" stroke="var(--line)" stroke-width="19">
      <rect x="22" y="33" width="1156" height="559"/>
      <line x1="600" y1="33" x2="600" y2="592"/>
      <rect x="22" y="182" width="116" height="240"/>
      <rect x="1055" y="182" width="145" height="240"/>
    </g>
    <circle cx="598" cy="317" r="160" fill="var(--circle-fill)"/>
    <circle cx="1069" cy="494" r="274" fill="var(--red)"/>
  </svg>

  <div class="cup-mark">
    <span class="square"></span>
    <div class="name">BRENNER &amp; KLUGE<br>CUP</div>
  </div>

  <div class="badge band">LUCKY<br>PUNCH</div>
  <div class="badge club">SpVgg<br>Wendelsau</div>

  <div class="venue"><span>Sportpark<br>Lindenwiese</span></div>

  <div class="schedule">
    <div class="date">07. - 09.06.<br>2024</div>
    <div class="day"><div class="label">FREITAG</div>Elfmeterturnier mit Live-Band</div>
    <div class="day"><div class="label">SAMSTAG</div>Jugendturnier F- und C- Jugend Vormittags und<br>E-Jugend Nachmittags</div>
    <div class="day"><div class="label">SONNTAG</div>Jugendturnier B- und D- Jugend Vormittags<br>und F3-Jugend Nachmittags</div>
    <div class="welcome">Besucher sind Willkommen;<br>Leibliche Wohl ist gesorgt.</div>
  </div>
</div>
</body>
</html>
```